Hacienda Las Verbenas Website

I need a template design for Hacienda Las Verbenas which is a Residential and Commercial development project to be located in Panama.

The look of the website has to be "country" since it is a Hacienda. It has to take in the feel of being out with nature.

The Logo of the project is contained in the attached files as well as pictures of the Project´s conceptual design and several air pictures of the land where the project will be built.

Industry/Entity Type

Residential

Requirements
Must have
• The website has to be very simple, very visual, a lot of images. The Main Menu has to be:
1. Home
2. About us
3. The project
4. Location
5. Contact us

```html
<!DOCTYPE html>
<html lang="en">
<head>
<meta charset="utf-8">
<title>Hacienda Las Verbenas</title>
<link href="https://fonts.googleapis.com/css2?family=Lora:wght@400;700&family=Arimo:wght@400;700&family=Open+Sans:wght@300;400&display=swap" rel="stylesheet">
<style>
:root{
  --nav-bg:#1c1510;
  --band-bg:#2a1d12;
  --accent:#c5742a;
  --accent-dark:#9c5418;
  --ink:#2b2b2b;
  --muted:#5a5a5a;
  --grey-band:#c9c8c4;
  --white:#ffffff;
  --cream:#f3e6d2;
}
*{margin:0;padding:0;box-sizing:border-box}
html,body{width:732px;height:1200px;overflow:hidden;background:var(--white)}
body{font-family:"Arimo",Arial,sans-serif;color:var(--ink);position:relative}
.top-nav{position:absolute;top:0;left:0;width:732px;height:22px;background:var(--nav-bg);display:flex;justify-content:center;align-items:center;gap:18px;z-index:3}
.top-nav a{font-size:10px;color:#cfc4b6;text-decoration:none}
.top-nav a.current{color:var(--white);font-weight:700}
.hero{position:absolute;top:0;left:0;width:732px;height:410px;background:linear-gradient(180deg,#b9b3a0 0%,#8d8a63 30%,#6f7444 60%,#5c5f38 100%)}
.hero-brand{position:absolute;top:32px;left:50%;transform:translateX(-50%);display:flex;align-items:center;gap:6px;background:var(--band-bg);padding:5px 9px;border-radius:4px}
.hero-brand .mark{width:10px;height:10px;background:var(--accent)}
.hero-brand span{font-family:"Lora",Georgia,serif;font-size:11px;color:var(--cream)}
.hero-title{position:absolute;top:220px;width:100%;text-align:center;font-family:"Lora",Georgia,serif;font-weight:700;font-size:30px;color:var(--white);text-shadow:0 2px 4px rgba(0,0,0,.5)}
.hero-lead{position:absolute;top:266px;left:110px;width:512px;text-align:center;font-size:13px;line-height:15px;color:var(--white);text-shadow:0 1px 3px rgba(0,0,0,.6)}
.hero-arrow{position:absolute;top:290px}
.hero-arrow.prev{left:14px}
.hero-arrow.next{right:14px}
.intro-band{position:absolute;top:410px;left:0;width:732px;height:140px;background:var(--band-bg);text-align:center}
.intro-band p{width:640px;margin:16px auto 0;font-size:11.5px;line-height:14px;color:#e8ddcf}
.quote-btn{display:inline-flex;align-items:center;gap:8px;margin-top:18px;background:#6b4a2b;border:1px solid #8a6642;border-radius:4px;padding:8px 16px;color:var(--cream);font-size:14px}
.feature{position:absolute;top:570px;left:0;width:732px;text-align:center}
.feature h2{font-family:"Lora",Georgia,serif;font-weight:700;font-size:24px;color:var(--accent)}
.feature .subhead{font-family:"Open Sans",Arial,sans-serif;font-weight:300;font-size:24px;color:var(--accent);margin-top:2px}
.feature .subhead mark{background:var(--accent);color:var(--white);padding:0 4px}
.feature p{width:680px;margin:10px auto 0;font-size:11.5px;line-height:14px;color:var(--ink)}
.gallery{position:absolute;top:690px;left:0;width:732px;height:240px}
.gallery .path{position:absolute;left:0;top:0}
.shot{position:absolute;box-shadow:0 10px 14px rgba(0,0,0,.25);border:3px solid var(--white)}
.shot.garden{left:26px;top:20px;width:172px;height:150px;border-radius:30px;background:radial-gradient(circle at 50% 55%,#3f6b2e 0%,#5f8f47 45%,#c9d1c4 80%)}
.shot.gate{left:300px;top:12px;width:132px;height:170px;border-radius:26px;background:linear-gradient(180deg,#bcd6ea 0%,#d9e6ef 45%,#8a5d3c 60%,#6f8f4c 100%)}
.shot.street{left:570px;top:24px;width:142px;height:120px;border-radius:24px;background:linear-gradient(180deg,#c5dbea 0%,#7ea05a 50%,#9b9b92 100%)}
.info-band{position:absolute;top:955px;left:0;width:732px;height:185px;background:var(--grey-band);padding:28px 26px 0}
.info-band h3{font-family:"Open Sans",Arial,sans-serif;font-weight:300;font-size:26px;color:var(--white)}
.info-band p{font-size:9.5px;line-height:12px;color:var(--white);margin-top:8px}
.site-footer{position:absolute;top:1140px;left:0;width:732px;height:60px;background:var(--white);display:flex;justify-content:space-between;align-items:center;padding:0 26px}
.footer-brand{display:flex;align-items:center;gap:8px}
.footer-brand .mark{width:28px;height:28px;background:var(--accent-dark)}
.footer-brand span{font-family:"Lora",Georgia,serif;font-size:22px;color:var(--accent)}
.footer-meta{text-align:right}
.footer-meta nav{display:flex;gap:14px;justify-content:flex-end}
.footer-meta a{font-size:9.5px;color:var(--ink);text-decoration:none}
.footer-meta small{display:block;font-size:9px;color:var(--muted);margin-top:4px}
</style>
</head>
<body>
<nav class="top-nav">
  <a class="current" href="#">home</a>
  <a href="#">about us</a>
  <a href="#">the project</a>
  <a href="#">location</a>
  <a href="#">contact us</a>
</nav>

<header class="hero" role="img" aria-label="Aerial photograph of the green hilly land where the development will be built">
  <div class="hero-brand"><div class="mark"></div><span>Las Verbenas</span></div>
  <h1 class="hero-title">Residential and Commercial development</h1>
  <p class="hero-lead">Lorem ipsum dolor sit amet, <b>consectetuer adipiscing elit, sed diam nonummy</b> nibh euismod tincidunt ut laoreet dolore magna aliquam erat volutpat.</p>
  <svg class="hero-arrow prev" width="22" height="16" viewBox="0 0 22 16"><path d="M20 8H3M9 2L3 8l6 6" fill="none" stroke="#fff" stroke-width="2"/></svg>
  <svg class="hero-arrow next" width="22" height="16" viewBox="0 0 22 16"><path d="M2 8h17M13 2l6 6-6 6" fill="none" stroke="#fff" stroke-width="2"/></svg>
</header>

<section class="intro-band">
  <p>Lorem ipsum dolor sit amet, ei dicit dolor vel, ea nec paulo facilis indoctum. <b>Sea tation melius neglegentur eu.</b> Ea sea facer noster probatus. In inani molestie has. Mel eu nusquam salutandi, eum nulla dicit et. Cum ea iusto prodesset, at velit singulis duo. In graeci quidam definitiones vix.</p>
  <span class="quote-btn">
    <svg width="14" height="14" viewBox="0 0 14 14"><path d="M3 1h6l3 3v9H3z" fill="none" stroke="#f3e6d2" stroke-width="1.3"/></svg>
    Ask for a quote
  </span>
</section>

<section class="feature">
  <h2>Modus clita iudico et mei.</h2>
  <div class="subhead">No facer <mark>contentiones</mark> consequuntur eam autem</div>
  <p>Lorem ipsum dolor sit amet, ei dicit dolor vel, ea nec paulo facilis indoctum. Sea tation melius neglegentur eu. Ea sea facer noster probatus. In inani molestie has. <b>Mel eu nusquam salutandi, eum nulla dicit et.</b> Cum ea iusto prodesset, at velit singulis duo. In graeci quidam definitiones vix.</p>
</section>

<section class="gallery">
  <svg class="path" width="732" height="240" viewBox="0 0 732 240"><path d="M0 150 C120 60 220 200 366 110 S600 50 732 120" fill="none" stroke="#bdbdbd" stroke-width="1.5" stroke-dasharray="6 5"/></svg>
  <div class="shot garden" role="img" aria-label="Rendering of a round landscaped garden plaza"></div>
  <div class="shot gate" role="img" aria-label="Rendering of the hacienda entrance gate tower"></div>
  <div class="shot street" role="img" aria-label="Rendering of a residential street with houses"></div>
</section>

<section class="info-band">
  <h3>Modus clita iudico</h3>
  <p>Tation nihil ea definitiones sea, ius quem facilisi ex. Per pertinax suscipit at, nam utroque salutandi id, mea cu nobis graeci fierent. Vis consul democritum, ex solet vituperata sed. Mea mentitum maiestatis an, his tale populo iudicabit cu, nec iisque option.</p>
  <p>Et nisl putent ius, ne eam alii regione persequeris. Sed tibique epicurei efficiantur ut, qui tantas verear copiosae eu. Duo autem nemore tamquam at, ut adhuc expetenda sit. Vidit aliquid ad nec, nec partem graeci.</p>
</section>

<footer class="site-footer">
  <div class="footer-brand"><div class="mark"></div><span>Las Verbenas</span></div>
  <div class="footer-meta">
    <nav>
      <a href="#">home</a><a href="#">about us</a><a href="#">the project</a><a href="#">location</a><a href="#">contact us</a>
    </nav>
    <small>© Copyright 2013 by Las Verbenas Hacienda. All Rights Reserved.</small>
  </div>
</footer>
</body>
</html>
```